Labels/logo for luxury bath products

I am developing a range of luxury bath foams - aimed at the top end of the luxury market. My company name is VRE (very basic website can be seen at www.vremarket.example).

I am looking for a label design for the front of the bottle, which should incorporate the VRE logo as per the website (file attached), but embedded within a more intricate label design. I provide a link to a picture of the bottle below.

The bath foam will come in four fragrances: Vetiver, Sandalwood, Jasmine and Neroli. The label should include the fragrance name. So the label must include the brand name 'VRE' and the name of the fragrance - e.g. Sandalwood Bath Foam, Neroli Bath Foam, etc.

The products are aimed at both the male and female market and so shouldn't be too feminine.

A brand to take inspiration from is Mabel Fenwick: http://www.mabelfenwick.example/ - I like the labels that they use on their products, which is a gold embossed crest, which they use as the label for their products. I am not referring to their font, but to their label design - I like the embossed label, and am quite keen on metallics.

Conversely, I would like to add a contemporary edge to this design - I like the striping and contemporary fonts on this design: http://www.tamsin-gale.example/images/qbx41.jpg

My brand also harnesses the powers of natural flower ingredients, and so I am inspired by the products of Ylvane - ylvane.example. This labelling is more clinical and scientific.

Ideally I would like a label which combines these elements - i.e. a luxury label with a contemporary feel, that incorporate the scientific nature of the product.

The design needs to communicate high end luxury. The bottle is however apothecary style, and a nod to science and botany would be good. I would however like a bold approach to this design - it is a modern brand.

The bottle being used for the product can be seen at: http://www.brevik-flask.example/en/product-groups/8-Apothecary-bottles - these are extremely expensive bottles and the label needs to reflect this quality. These bottles are traditional in design, but incorporate high end glassware technology to preserve the integrity of the natural ingredients. Therefore the product is a mix of old and new, and the label could also reflect this. The colour of the glass is very deep purple.

The front label does not need information such as weight/volume - it purely needs a label which will recognise it as the VRE brand, with the product name. I am looking for a high quality label, which is unique. I am happy to print embossed labels and to use foils on my labels.

Please do not be boring! I appreciate I have given a variety of influences, so summarise the requirements are a mix of:

a bold design
contemporary
luxury

The label must include NO slogans.

I am looking to build a relationship with a graphic designer for packaging and website design requirements so this will be the first of many projects.

Target Market(s)

Luxury end of market - clientele will like luxury and will pay for the highest quality ingredients in the product, but will also appreciate the botanical nature of the product.

Industry/Entity Type

Graphic Designer

Requirements
Must have
• Must include the company name, VRE, although this doesn't need to be particularly prominent. And the product name, e.g. Sandalwood.
Nice to have
• It should combine luxury, but with recognition of the science behind the product.
Should not have
• No slogans, minimal wording on the front label. No other wording other than company name and product name. No primary colours.

```html
<!DOCTYPE html>
<html lang="en">
<head>
<meta charset="utf-8">
<title>VRE Bath Foam Labels</title>
<link rel="stylesheet" href="https://fonts.googleapis.com/css2?family=Archivo+Black&family=Playfair+Display:wght@400;500&display=swap">
<style>
  :root {
    --page-bg: #ffffff;
    --gold-light: #f7e08a;
    --gold-mid: #e3b53a;
    --gold-deep: #b8862a;
    --gold-edge: #c99a3a;
    --ink: #111111;
    --sandalwood: #c3a06e;
    --jasmine: #ffffff;
    --vetiver: #8cf01e;
    --neroli: #a35ad6;
  }
  html, body {
    margin: 0;
    padding: 0;
    width: 1200px;
    height: 900px;
    overflow: hidden;
    background: var(--page-bg);
  }
  .label-range {
    position: relative;
    width: 1200px;
    height: 900px;
  }
  .label {
    position: absolute;
    top: 292px;
    width: 156px;
    height: 315px;
    margin-left: -78px;
    box-sizing: border-box;
    background: linear-gradient(100deg, var(--gold-deep) 0%, var(--gold-light) 28%, var(--gold-mid) 55%, var(--gold-light) 78%, var(--gold-deep) 100%);
    box-shadow: inset 0 0 0 2px var(--gold-edge);
  }
  .label--sandalwood { left: 153px; }
  .label--jasmine { left: 451px; }
  .label--vetiver { left: 749px; }
  .label--neroli { left: 1047px; }
  .brand-name {
    position: absolute;
    top: 66px;
    left: 0;
    width: 100%;
    text-align: center;
    font-family: "Archivo Black", "Arial Black", sans-serif;
    font-size: 56px;
    line-height: 1;
    letter-spacing: -2px;
    color: var(--ink);
  }
  .fragrance-band {
    position: absolute;
    top: 160px;
    left: 50%;
    width: 262px;
    height: 75px;
    margin-left: -131px;
    box-sizing: border-box;
    border: 5px solid var(--gold-mid);
    border-radius: 5px;
    display: flex;
    align-items: center;
    justify-content: center;
    font-family: "Playfair Display", Georgia, serif;
    font-size: 38px;
    line-height: 1;
    color: var(--ink);
    white-space: nowrap;
  }
  .fragrance-band--sandalwood { background: var(--sandalwood); }
  .fragrance-band--jasmine { background: var(--jasmine); }
  .fragrance-band--vetiver { background: var(--vetiver); }
  .fragrance-band--neroli { background: var(--neroli); }
  .product-type {
    position: absolute;
    top: 262px;
    left: 0;
    width: 100%;
    text-align: center;
    font-family: "Playfair Display", Georgia, serif;
    font-size: 18px;
    font-weight: 500;
    line-height: 1;
    color: var(--ink);
  }
</style>
</head>
<body>
  <main class="label-range">
    <div class="label label--sandalwood">
      <div class="brand-name">VRE</div>
      <div class="fragrance-band fragrance-band--sandalwood">Sandalwood</div>
      <div class="product-type">BATH FOAM</div>
    </div>
    <div class="label label--jasmine">
      <div class="brand-name">VRE</div>
      <div class="fragrance-band fragrance-band--jasmine">Jasmine</div>
      <div class="product-type">BATH FOAM</div>
    </div>
    <div class="label label--vetiver">
      <div class="brand-name">VRE</div>
      <div class="fragrance-band fragrance-band--vetiver">Vetiver</div>
      <div class="product-type">BATH FOAM</div>
    </div>
    <div class="label label--neroli">
      <div class="brand-name">VRE</div>
      <div class="fragrance-band fragrance-band--neroli">Neroli</div>
      <div class="product-type">BATH FOAM</div>
    </div>
  </main>
</body>
</html>
```